political campaign lawn sign - Governor's Council in Massachuesetts

We are looking for a political lawn sign. We are running a campaign for Governor's Council in Massachusetts. This sign will be on the lawn of homes and businesses so people driving by will see it. It needs to be simple and bold. The last name is long so maybe it could say vote for Marty and then Kolbeck will be big a bold on the next line??
We need it to say:
Vote for Martin Kolbeck
Governor's Council.

Target Market(s)

local residents

Industry/Entity Type

Politcal Campaign

Font styles to use
Sans Serif
Other font styles liked:
• not sure what font but a modern looking one such as Helvetica, Arial, Sans Seri, sharp sans..

Colors
0054AA
0677BA
7BADD7
CADEEF
E8F1F8
00AB8E
00BBA5
67D7C9
C6EFE9
E9F9F6
FFF300
FFF600
FEFA6F
FFFEC7
FFFEE8

Requirements
Must have
• My name written out with a Capital D and R but lower case for every other letter so its Marty Kolbeck
Nice to have
• modern font , the Colors of the lawn sign should have Blue, Yellow and White something bold that will stand out
Should not have
• any maps of Massachusetts

```html
<!DOCTYPE html>
<html lang="en">
<head>
<meta charset="utf-8">
<title>Vote for Marty Kolbeck – Lawn Sign</title>
<link href="https://fonts.googleapis.com/css2?family=Montserrat:wght@600;700;800;900&display=swap" rel="stylesheet">
<style>
  :root {
    --navy: #001a4b;
    --yellow: #ffd200;
    --white: #ffffff;
    --sign-white: #eceef0;
    --backdrop: #dfe6ec;
  }
  * { margin: 0; padding: 0; box-sizing: border-box; }
  html, body {
    width: 1200px; height: 1133px; overflow: hidden;
    background: var(--backdrop);
    font-family: "Montserrat", Arial, sans-serif;
  }
  .sign {
    position: absolute; left: 100px; top: 136px;
    width: 1000px; height: 860px;
    background: var(--sign-white);
    overflow: hidden;
  }
  .sign-wave { position: absolute; inset: 0; width: 1000px; height: 860px; }
  .sign-content { position: absolute; inset: 0; color: var(--white); }

  .kicker {
    position: absolute; top: 120px; left: 0; width: 100%;
    display: flex; align-items: center; justify-content: center; gap: 28px;
  }
  .kicker-rule { width: 190px; height: 5px; background: var(--white); }
  .kicker-text {
    font-weight: 600; font-size: 72px; letter-spacing: 6px; line-height: 1;
  }

  .first-name-row {
    position: absolute; top: 200px; left: 0; width: 100%;
    display: flex; align-items: center; justify-content: center; gap: 36px;
  }
  .star-pair { display: flex; gap: 16px; }
  .star-pair svg { width: 78px; height: 78px; fill: var(--white); }
  .star-pair--left { margin-top: -40px; }
  .star-pair--right { margin-top: 60px; }
  .first-name {
    font-weight: 800; font-size: 170px; line-height: 1; letter-spacing: -2px;
  }

  .last-name {
    position: absolute; top: 355px; left: 0; width: 100%;
    text-align: center; color: var(--yellow);
    font-weight: 900; font-size: 210px; line-height: 1; letter-spacing: -2px;
  }

  .divider {
    position: absolute; top: 580px; left: 110px; width: 780px; height: 5px;
    background: var(--white);
  }
  .office {
    position: absolute; top: 605px; left: 0; width: 100%;
    text-align: center; font-weight: 700; font-size: 54px; letter-spacing: 7px; line-height: 1;
  }

  .web-address {
    position: absolute; top: 770px; left: 0; width: 100%;
    text-align: center; color: var(--navy);
    font-weight: 800; font-size: 66px; letter-spacing: 7px; line-height: 1;
  }
</style>
</head>
<body>
  <div class="sign">
    <svg class="sign-wave" viewBox="0 0 1000 860" aria-hidden="true">
      <path d="M0 680 C 200 740 360 780 560 772 C 760 764 860 730 1000 732 L1000 0 L0 0 Z" fill="var(--yellow)"/>
      <path d="M0 662 C 200 722 360 762 560 754 C 760 746 860 712 1000 714 L1000 0 L0 0 Z" fill="var(--navy)"/>
    </svg>

    <div class="sign-content">
      <div class="kicker">
        <span class="kicker-rule"></span>
        <span class="kicker-text">VOTE FOR</span>
        <span class="kicker-rule"></span>
      </div>

      <div class="first-name-row">
        <div class="star-pair star-pair--left">
          <svg viewBox="0 0 24 24"><polygon points="12,1 15,9 23.5,9 16.5,14 19,22.5 12,17.5 5,22.5 7.5,14 0.5,9 9,9"/></svg>
          <svg viewBox="0 0 24 24"><polygon points="12,1 15,9 23.5,9 16.5,14 19,22.5 12,17.5 5,22.5 7.5,14 0.5,9 9,9"/></svg>
        </div>
        <span class="first-name">Marty</span>
        <div class="star-pair star-pair--right">
          <svg viewBox="0 0 24 24"><polygon points="12,1 15,9 23.5,9 16.5,14 19,22.5 12,17.5 5,22.5 7.5,14 0.5,9 9,9"/></svg>
          <svg viewBox="0 0 24 24"><polygon points="12,1 15,9 23.5,9 16.5,14 19,22.5 12,17.5 5,22.5 7.5,14 0.5,9 9,9"/></svg>
        </div>
      </div>

      <div class="last-name">Kolbeck</div>
      <div class="divider"></div>
      <div class="office">GOVERNER'S COUNCIL</div>
      <div class="web-address">VOTEFORMARTY.NET</div>
    </div>
  </div>
</body>
</html>
```